Piano genealogy graphs template, for a large poster printing

Hello and thank you for your interest in my project.
I need a poster template, so I can create structures similar to the one I have uploaded. I want to completely replace or improve my poor previous design which is attached.
I need to be able to input names and dates into boxes of various colors, arrows pointing between boxes. I would also like to be able to label each graph (not each box).
I am looking at something that would be legible when printed, in a one consistent professional layout of 2A0 (around 1189x1682 mm) poster (I know it is large). The design template required here can include just few sample text boxes with sample flags on a suitable background, for me to multiply later and spread across the whole poster.
The positioning of the boxes is not important.
Please let me know if more clarification is required.
Thank you for your help.

Feel free to follow what I have attached in the file, or change the design completely.

UPDATE 4/12: I have uploaded two more graphs as an example. At this stage of the contest, I would like to have one of those graphs done, and I am planning to offer a 'freelance job' to one or two designers, who will be willing to do the whole 10 graphs on one poster.
Updates

Reason: Dear Designers, Since the project is rather complex and large-scale, I have decided to give everyone more time to work on their designs. I will consider extending it further if any of you require additional time. Best wishes, bronisław

Dear Designers, I would like to inform you that the contest for my poster is now closed and that I have assigned the prizes. I would like to thank all of you for submiting your high-quality designs, and for your participation. It was a great pleasure working with all of you. Due to the large size of the project itself (large number of graphs to be fitted on a single poster), I had to focus on providing feedback to only those designers who provided projects closest to what I was expecting at the early stages of the contest. I wish you all the best for the future, Kind regards, Bronisław

Target Market(s)

Pianists, historians

Industry/Entity Type

Printing

Requirements
Must have
• Consistent design, but allow to clearly delineate various genealogy trees.

```html
<!DOCTYPE html>
<html lang="en">
<head>
<meta charset="utf-8">
<title>Genealogical Trees of Pianists</title>
<link rel="stylesheet" href="https://fonts.googleapis.com/css2?family=Great+Vibes&family=Oswald:wght@300;400&family=PT+Sans+Narrow&display=swap">
<style>
  :root {
    --bg-centre: #2b2b2b;
    --bg-edge: #020202;
    --ink: #ffffff;
    --ink-soft: #dcdcdc;
    --frame: #8a8a8a;
    --flourish: #6b6b6b;
    --us-red: #c8313b;
    --us-blue: #2b3f86;
    --pl-red: #d4213d;
    --it-green: #0f8a45;
    --it-red: #cd212a;
    --hu-red: #ce2939;
    --hu-green: #477050;
    --de-black: #111;
    --de-red: #dd0000;
    --de-gold: #ffce00;
    --gb-blue: #243b7a;
    --il-blue: #1f49b5;
  }
  * { margin: 0; padding: 0; box-sizing: border-box; }
  html, body { width: 848px; height: 1200px; overflow: hidden; background: var(--bg-edge); }
  .poster {
    position: relative; width: 848px; height: 1200px; overflow: hidden;
    background: radial-gradient(ellipse 75% 55% at 50% 45%, var(--bg-centre), var(--bg-edge));
    color: var(--ink);
    font-family: "Oswald", sans-serif; font-weight: 300;
  }
  .title-ornament {
    position: absolute; left: 215px; top: 4px; width: 465px; height: 108px;
    background: radial-gradient(ellipse at 50% 45%, rgba(120,120,120,.35), rgba(60,60,60,.12) 60%, transparent 75%);
  }
  .title { position: absolute; left: 0; top: 32px; width: 848px; text-align: center; font-family: "Great Vibes", cursive; font-weight: 400; }
  .title-small { display: block; font-size: 32px; line-height: 34px; padding-left: 120px; }
  .title-large { display: block; font-size: 74px; line-height: 64px; margin-left: -90px; }

  .branch-heading {
    position: absolute; left: 0; width: 848px; display: flex; justify-content: center; align-items: center; gap: 12px;
    font-family: "PT Sans Narrow", sans-serif; font-size: 23px; color: var(--ink);
  }
  .flourish { display: inline-block; width: 22px; height: 8px; border-radius: 50%;
    background: radial-gradient(ellipse, var(--flourish), transparent 70%); }
  .flag-band { position: absolute; height: 12px; }
  .flag-band.italy { left: 460px; top: 189px; width: 134px;
    background: linear-gradient(90deg, var(--it-green) 0 33.3%, #fff 33.3% 66.6%, var(--it-red) 66.6%); }
  .flag-band.hungary { left: 443px; top: 811px; width: 163px; height: 15px;
    background: linear-gradient(180deg, var(--hu-red) 0 33.3%, #fff 33.3% 66.6%, var(--hu-green) 66.6%); }

  .node { position: absolute; transform: translateX(-50%); text-align: center; padding: 4px 15px;
    font-size: 9px; line-height: 11px; color: var(--ink-soft); white-space: nowrap; }
  .node::before, .node::after { content: ""; position: absolute; top: 2px; bottom: 2px; width: 9px; border: 1px solid var(--frame); }
  .node::before { left: 0; border-right: none; border-radius: 50% 0 0 50%; }
  .node::after { right: 0; border-left: none; border-radius: 0 50% 50% 0; }
  .node.teacher { padding: 2px 22px; }
  .node.teacher::before, .node.teacher::after { top: 40%; bottom: 40%; }
  .teacher-name { color: var(--ink); }

  .flag { display: inline-block; width: 10px; height: 6px; margin-right: 2px; vertical-align: 0; }
  .flag.us { background: linear-gradient(90deg, var(--us-blue) 0 40%, transparent 40%), repeating-linear-gradient(180deg, var(--us-red) 0 1px, #fff 1px 2px); }
  .flag.pl { background: linear-gradient(180deg, #fff 50%, var(--pl-red) 50%); }
  .flag.it { background: linear-gradient(90deg, var(--it-green) 0 33%, #fff 33% 66%, var(--it-red) 66%); }
  .flag.hu { background: linear-gradient(180deg, var(--hu-red) 0 33%, #fff 33% 66%, var(--hu-green) 66%); }
  .flag.de { background: linear-gradient(180deg, var(--de-black) 0 33%, var(--de-red) 33% 66%, var(--de-gold) 66%); }
  .flag.gb { background: linear-gradient(90deg, transparent 42%, var(--us-red) 42% 58%, transparent 58%), linear-gradient(180deg, var(--gb-blue) 35%, var(--us-red) 35% 65%, var(--gb-blue) 65%); }
  .flag.il { background: linear-gradient(180deg, #fff 15%, var(--il-blue) 15% 30%, #fff 30% 70%, var(--il-blue) 70% 85%, #fff 85%); }
  .flag.kr { background: radial-gradient(circle, var(--us-red) 0 22%, var(--us-blue) 22% 38%, #fff 38%); }

  .keyboard { position: absolute; left: 0; top: 1035px; width: 848px; height: 165px;
    background: linear-gradient(180deg, #1a1a1a 0 12%, #f2f2f2 12% 30%, #d9d9d9 70%, #8a8a8a 100%); }
</style>
</head>
<body>
<main class="poster">
  <div class="title-ornament" role="img" aria-label="Ornamental scroll flourish behind the title"></div>
  <h1 class="title"><span class="title-small">Genealogical Trees of</span><span class="title-large">Pianists</span></h1>

  <!-- Branch II -->
  <h2 class="branch-heading" style="top:157px"><span class="flourish" role="img" aria-label="Flourish"></span>American Tree, Branch II - Italian influences<span class="flourish" role="img" aria-label="Flourish"></span></h2>
  <div class="flag-band italy"></div>

  <div class="node teacher" style="left:240px;top:230px">
    <div class="teacher-name"><span class="flag us"></span>Daniel Sorrento</div><div>(1889-1970) Students:</div>
    <div><span class="flag us"></span>Charles Rowan (1927-2012)</div><div><span class="flag us"></span>Sidney Larkin (1927)</div>
    <div><span class="flag us"></span>Abel Simms (1922)</div><div><span class="flag us"></span>Jorge Balart (1914-1990)</div>
    <div><span class="flag de"></span><span class="flag us"></span>Claude Fenner (1925-2014)</div><div><span class="flag us"></span>Eleanor Sorokin (1914)</div>
    <div><span class="flag us"></span>Sasha Chernova (1909-1995)</div>
  </div>
  <div class="node teacher" style="left:424px;top:235px">
    <div class="teacher-name"><span class="flag it"></span>Edmund Steinhart (1892-1964)</div><div>Students:</div>
    <div><span class="flag us"></span>Joseph Kalmanson (1946)</div><div><span class="flag us"></span>Baruch Alder (1990)</div>
    <div><span class="flag us"></span>Jerome Lindqvist (1932)</div><div><span class="flag us"></span>Alfred Brenner (1931)</div>
    <div><span class="flag us"></span><span class="flag kr"></span>Russell Shelton (1930)</div><div><span class="flag gb"></span>Maura Lindley (1916-2005)</div>
    <div>Irwin Friedberg (1908-1977)</div><div>Jakob Gerstel (1906-1989)</div>
  </div>
  <div class="node teacher" style="left:605px;top:230px">
    <div class="teacher-name"><span class="flag us"></span>Marina Corsetti</div><div>(1889-1970) Students:</div>
    <div><span class="flag us"></span>Charles Rowan (1927-2012)</div><div><span class="flag us"></span>Sidney Larkin (1927)</div>
    <div><span class="flag us"></span>Claude Fenner (1925-2014)</div><div><span class="flag us"></span>Abel Simms (1922)</div>
    <div><span class="flag us"></span>Jorge Balart (1914-1990)</div><div><span class="flag us"></span>Eleanor Sorokin (1914)</div>
    <div><span class="flag us"></span>Sasha Chernova (1909-1995)</div>
  </div>

  <div class="node teacher" style="left:160px;top:381px">
    <div class="teacher-name"><span class="flag us"></span>Guido Albani</div><div>(1901-1989) Students:</div>
    <div><span class="flag il"></span><span class="flag us"></span>Horacio Gallardo (1948)</div><div>Dennis Pollard (1935)</div>
    <div><span class="flag us"></span>Raymond Lederer (1923-1988)</div><div><span class="flag us"></span>Julian Marsh</div>
  </div>
  <div class="node" style="left:330px;top:405px"><div><span class="flag us"></span>Carlo Zanetti</div><div>(1903-1984)</div></div>
  <div class="node" style="left:425px;top:405px"><div><span class="flag us"></span>Carlo Zanetti</div><div>(1903-1984)</div></div>
  <div class="node" style="left:517px;top:405px"><div><span class="flag us"></span>Carlo Zanetti</div><div>(1903-1984)</div></div>
  <div class="node" style="left:612px;top:405px"><div><span class="flag us"></span>Carlo Zanetti</div><div>(1903-1984)</div></div>
  <div class="node" style="left:718px;top:405px"><div><span class="flag us"></span>Carlo Zanetti</div><div>(1903-1984)</div></div>

  <!-- Branch III -->
  <h2 class="branch-heading" style="top:479px"><span class="flourish" role="img" aria-label="Flourish"></span>American Tree, Branch III - Varenne and Kovach<span class="flourish" role="img" aria-label="Flourish"></span></h2>

  <div class="node" style="left:165px;top:543px"><div><span class="flag us"></span>Carlo Zanetti</div><div>(1903-1984)</div></div>
  <div class="node" style="left:165px;top:617px"><div><span class="flag us"></span>Carlo Zanetti</div><div>(1903-1984)</div></div>
  <div class="node teacher" style="left:315px;top:525px">
    <div class="teacher-name"><span class="flag pl"></span>Guido Albani</div><div>(1901-1989) Students:</div>
    <div><span class="flag pl"></span>Horacio Gallardo (1948)</div><div><span class="flag pl"></span>Dennis Pollard (1935)</div>
    <div><span class="flag pl"></span>Raymond Lederer (1923-1988)</div><div><span class="flag us"></span>Julian Marsh</div>
  </div>
  <div class="node" style="left:315px;top:645px"><div><span class="flag pl"></span>Carlo Zanetti</div><div>(1903-1984)</div></div>
  <div class="node" style="left:425px;top:645px"><div><span class="flag us"></span>Carlo Zanetti</div><div>(1903-1984)</div></div>
  <div class="node" style="left:315px;top:709px"><div><span class="flag pl"></span>Carlo Zanetti</div><div>(1903-1984)</div></div>
  <div class="node" style="left:425px;top:709px"><div><span class="flag us"></span>Carlo Zanetti</div><div>(1903-1984)</div></div>
  <div class="node" style="left:585px;top:537px"><div><span class="flag de"></span>Carlo Zanetti</div><div>(1903-1984)</div></div>
  <div class="node" style="left:685px;top:537px"><div><span class="flag us"></span>Carlo Zanetti</div><div>(1903-1984)</div></div>
  <div class="node" style="left:585px;top:600px"><div><span class="flag de"></span>Carlo Zanetti</div><div>(1903-1984)</div></div>
  <div class="node" style="left:685px;top:600px"><div><span class="flag us"></span>Carlo Zanetti</div><div>(1903-1984)</div></div>
  <div class="node" style="left:585px;top:659px"><div><span class="flag us"></span>Carlo Zanetti</div><div>(1903-1984)</div></div>

  <!-- Branch IV -->
  <h2 class="branch-heading" style="top:780px"><span class="flourish" role="img" aria-label="Flourish"></span>American Tree, Branch IV Hungarian influences<span class="flourish" role="img" aria-label="Flourish"></span></h2>
  <div class="flag-band hungary"></div>

  <div class="node teacher" style="left:195px;top:813px">
    <div class="teacher-name"><span class="flag pl"></span>Edmund Steinhart (1892-1964)</div><div>Students:</div>
    <div><span class="flag hu"></span>Joseph Kalmanson (1946)</div><div><span class="flag hu"></span>Baruch Alder (1990)</div>
    <div><span class="flag us"></span>Jerome Lindqvist (1932)</div><div><span class="flag us"></span>Alfred Brenner (1931)</div>
    <div><span class="flag de"></span>Russell Shelton (1930)</div><div><span class="flag il"></span>Maura Lindley (1916-2005)</div>
    <div><span class="flag gb"></span>Irwin Friedberg (1908-1977)</div><div><span class="flag de"></span>Jakob Gerstel (1906-1989)</div>
  </div>
  <div class="node teacher" style="left:343px;top:813px">
    <div class="teacher-name"><span class="flag hu"></span>Edmund Steinhart (1892-1964)</div><div>Students:</div>
    <div><span class="flag us"></span>Joseph Kalmanson (1946)</div><div><span class="flag gb"></span>Baruch Alder (1990)</div>
    <div><span class="flag us"></span>Jerome Lindqvist (1932)</div><div><span class="flag de"></span>Alfred Brenner (1931)</div>
    <div><span class="flag gb"></span>Russell Shelton (1930)</div><div><span class="flag us"></span>Maura Lindley (1916-2005)</div>
    <div><span class="flag us"></span>Irwin Friedberg (1908-1977)</div><div><span class="flag pl"></span>Jakob Gerstel (1906-1989)</div>
  </div>
  <div class="node" style="left:195px;top:1009px"><div><span class="flag gb"></span>Carlo Zanetti</div><div>(1903-1984)</div></div>
  <div class="node" style="left:343px;top:1009px"><div><span class="flag gb"></span>Carlo Zanetti</div><div>(1903-1984)</div></div>
  <div class="node" style="left:500px;top:847px"><div><span class="flag de"></span>Carlo Zanetti</div><div>(1903-1984)</div></div>
  <div class="node" style="left:595px;top:847px"><div><span class="flag us"></span>Carlo Zanetti</div><div>(1903-1984)</div></div>
  <div class="node" style="left:690px;top:847px"><div><span class="flag us"></span>Carlo Zanetti</div><div>(1903-1984)</div></div>
  <div class="node" style="left:595px;top:925px"><div><span class="flag gb"></span>Carlo Zanetti</div><div>(1903-1984)</div></div>
  <div class="node" style="left:595px;top:982px"><div><span class="flag de"></span>Carlo Zanetti</div><div>(1903-1984)</div></div>

  <div class="keyboard" role="img" aria-label="Piano keyboard seen in perspective along the bottom edge"></div>
</main>
</body>
</html>
```